Fitness Business Card Design Needed

We are looking for a business card design that stands out but is also simple and unique. I like the idea of on one side using the picture of myself with my logo at my feet. I love the texture on the business card so please take that into account when designing. Then on the other side having my contact details. I want it to be clean, modern, and pretty. I am open to designs that allow spot gloss or gold foiling.

Space for Name, Phone number, email, and website

```html
<!DOCTYPE html>
<html lang="en">
<head>
<meta charset="utf-8">
<title>PetitePower Fitness – Business Card</title>
<link href="https://fonts.googleapis.com/css2?family=Roboto:wght@400;500;700&display=swap" rel="stylesheet">
<style>
  :root{
    --bg:#1e1e20;
    --white:#ffffff;
    --ink:#2f2f2f;
    --rule:#6b6b6b;
    --gold:#b48a3c;
    --gold-light:#e9b463;
    --gold-mid:#c89a4e;
    --gold-dark:#96763e;
    --charcoal:#3a3a3c;
  }
  *{box-sizing:border-box;margin:0;padding:0}
  html,body{width:1200px;height:801px;overflow:hidden;background:var(--bg);font-family:'Roboto',sans-serif}
  .canvas{position:relative;width:1200px;height:801px}
  .card{position:absolute;width:580px;height:330px;overflow:hidden;box-shadow:0 8px 24px rgba(0,0,0,.45)}

  /* contact side */
  .card--contact{left:310px;top:40px;background:var(--white)}
  .brand{position:absolute;right:40px;top:62px;display:flex;align-items:center;gap:10px}
  .brand__mark{width:14px;height:14px;border:1.5px solid var(--gold)}
  .brand__name{font-size:17px;font-weight:400;letter-spacing:3px;color:var(--gold)}
  .person{position:absolute;left:40px;top:140px}
  .person__name{font-size:25px;font-weight:700;color:var(--gold);letter-spacing:.5px}
  .person__role{font-size:15px;color:var(--ink);margin-top:2px;letter-spacing:.3px}
  .divider{position:absolute;left:40px;right:40px;top:198px;height:1px;background:var(--rule)}
  .contact{position:absolute;left:40px;top:214px;list-style:none;font-size:14px;color:var(--ink)}
  .contact li{display:flex;align-items:center;gap:8px;height:20px}
  .contact svg{width:12px;height:12px;fill:var(--gold)}
  .address{position:absolute;right:40px;top:214px;text-align:right;font-size:15px;color:var(--ink);line-height:21px}
  .band{position:absolute;left:0;bottom:0;width:580px;height:58px}
  .band__url{position:absolute;right:40px;bottom:12px;font-size:16px;font-weight:500;color:var(--ink);letter-spacing:1px}

  /* photo side */
  .card--photo{left:310px;top:420px;background:radial-gradient(ellipse at 42% 40%,var(--gold-light) 0%,var(--gold-mid) 45%,var(--gold-dark) 100%)}
  .portrait{position:absolute;left:245px;top:20px;width:90px;height:230px;border-radius:40px 40px 10px 10px;background:linear-gradient(180deg,#e0b891 0%,#c98a6a 45%,#b97a58 100%);opacity:.9}
  .base{position:absolute;left:232px;top:240px;width:116px;height:14px;border-radius:50%;background:#d8cdbd}
  .photo-brand{position:absolute;left:0;right:0;top:268px;display:flex;justify-content:center;align-items:center;gap:10px}
  .photo-brand .brand__mark{border-color:var(--white)}
  .photo-brand .brand__name{color:var(--white);font-size:19px}
</style>
</head>
<body>
<main class="canvas">

  <section class="card card--contact" aria-label="Contact side">
    <div class="brand">
      <span class="brand__mark"></span>
      <span class="brand__name">PETITEPOWER FITNESS</span>
    </div>

    <div class="person">
      <h1 class="person__name">NORA WHITFIELD</h1>
      <p class="person__role">FITNESS TRAINER</p>
    </div>

    <div class="divider"></div>

    <ul class="contact">
      <li>
        <svg viewBox="0 0 24 24" aria-hidden="true"><path d="M6.6 10.8a15.1 15.1 0 0 0 6.6 6.6l2.2-2.2c.3-.3.7-.4 1-.2 1.1.4 2.3.6 3.6.6.6 0 1 .4 1 1V20c0 .6-.4 1-1 1A17 17 0 0 1 3 4c0-.6.4-1 1-1h3.5c.6 0 1 .4 1 1 0 1.3.2 2.5.6 3.6.1.3 0 .7-.2 1z"/></svg>
        555 014 2730
      </li>
      <li>
        <svg viewBox="0 0 24 24" aria-hidden="true"><path d="M2 5h20v14H2zm2 2v.5l8 5 8-5V7l-8 5z"/></svg>
        info@petitepowerfit.com
      </li>
    </ul>

    <address class="address" style="font-style:normal">
      1420 Willow Crest Road<br>
      Lakeside, Montana 59012
    </address>

    <svg class="band" viewBox="0 0 580 58" preserveAspectRatio="none" aria-hidden="true">
      <path d="M0 0 H580 V8 H440 Q420 8 410 20 L0 14 Z" fill="var(--charcoal)" opacity="0"/>
      <path d="M0 8 L405 14 Q418 6 438 6 H580 V10 H440 Q424 10 414 20 L0 16 Z" fill="var(--charcoal)"/>
      <path d="M0 16 L414 20 Q424 12 440 12 H580 V58 H0 Z" fill="var(--gold)"/>
      <path d="M0 18 L414 24 L414 58 H0 Z" fill="var(--white)"/>
    </svg>
    <span class="band__url">www.petitepowerfit.com</span>
  </section>

  <section class="card card--photo" aria-label="Photo side">
    <div class="portrait" role="img" aria-label="Full-length photo of the trainer in a red swimsuit, standing with hands on hips"></div>
    <div class="base" role="img" aria-label="Small patch of sand beneath the trainer's feet"></div>
    <div class="photo-brand">
      <span class="brand__mark"></span>
      <span class="brand__name">PETITEPOWER FITNESS</span>
    </div>
  </section>

</main>
</body>
</html>
```